Clear Plastic Business Card for Executives

We need a business card design for a national technology sales company that focuses on large and enterprise business. We handle every manufacturer and have clients as reputable as the KVT and Zuvora. We have a general idea of what we are looking for in the design, which is included. We are looking for a clear card, not frosted, with a microchip or motherboard design such as seen in the rough picture. The back will have select quotes we use. Our company logo is attached on the top left of the card which will be included on the card. The final design should communicate VIP level service and executive performance.
Target Market(s)
Technology executives, CIO's, CEO's
Industry/Entity Type
Business
Contact Information for Business Card
clear card for the executive level, name, office and mobile number, title, logo
Requirements
Must have
- Included RMZ logo, 2 sides, microchip/computer chip technology design, clear

```html
<!DOCTYPE html>
<html lang="en">
<head>
<meta charset="utf-8">
<title>RMZ Technologies – Business Card</title>
<link rel="stylesheet" href="https://fonts.googleapis.com/css2?family=Open+Sans:ital,wght@0,400;0,600;0,700;1,400;1,700&display=swap">
<style>
  :root{
    --bg:#8d8786;
    --card:#b2b0af;
    --card-edge:#c4c2c1;
    --band:#1d1d1d;
    --block:#5e5c5c;
    --ink:#151515;
    --ink-soft:#2c2c2c;
    --on-dark:#e6e6e6;
    --quote:#d2d2d2;
    --accent:#b3202a;
    --chip-core:#2a2a2c;
    --chip-mid:#8f9197;
    --trace:#9b9998;
  }
  *{box-sizing:border-box;margin:0;padding:0}
  html,body{width:1200px;height:800px;overflow:hidden}
  body{background:var(--bg);font-family:"Open Sans",Arial,sans-serif;position:relative}

  .card{
    position:absolute;top:240px;width:540px;height:310px;
    background:var(--card);border-radius:16px;overflow:hidden;
    box-shadow:0 0 0 1px var(--card-edge) inset,0 10px 24px rgba(0,0,0,.18);
  }
  .card--front{left:45px}
  .card--back{left:615px}

  /* front */
  .brand{position:absolute;left:32px;top:28px;display:flex;align-items:center;gap:9px}
  .brand__dot{width:12px;height:12px;border-radius:50%;background:var(--accent)}
  .brand__name{font-weight:700;font-size:19px;color:var(--ink);letter-spacing:.2px}
  .person{position:absolute;left:32px;top:96px}
  .person__name{font-weight:700;font-size:19px;color:var(--ink)}
  .person__title{font-size:12.5px;color:var(--ink-soft);margin-top:1px}

  .circuit-art{
    position:absolute;left:290px;top:50px;width:240px;height:178px;
    background:radial-gradient(ellipse 60% 62% at 56% 50%,var(--chip-core) 0 22%,var(--chip-mid) 34%,var(--trace) 55%,var(--card) 100%);
  }

  .contact-band{
    position:absolute;left:0;top:178px;width:390px;height:95px;background:var(--band);
    padding:16px 0 0 14px;color:var(--on-dark);font-size:13px;line-height:20px;
  }
  .contact-band__row{display:flex;align-items:center;gap:10px;white-space:nowrap}
  .contact-band__row svg{width:12px;height:12px;flex:none}
  .contact-band__phone2{display:inline-flex;align-items:center;gap:6px;margin-left:8px}

  .motto-block{
    position:absolute;left:390px;top:228px;width:150px;height:82px;background:var(--block);
    color:var(--on-dark);font-size:13px;font-style:italic;text-align:center;padding-top:30px;
  }

  /* back */
  .quote-band{position:absolute;left:0;top:70px;width:100%;height:66px;background:var(--band)}
  .quote{
    position:absolute;left:0;width:100%;top:160px;text-align:center;
    color:var(--quote);font-weight:700;font-style:italic;font-size:16px;
  }
  .quote__by{
    position:absolute;left:0;width:100%;top:188px;text-align:center;
    color:var(--ink-soft);font-size:10px;
  }
</style>
</head>
<body>

<section class="card card--front" aria-label="Card front">
  <div class="brand">
    <span class="brand__dot"></span>
    <span class="brand__name">RMZ Technologies, Inc.</span>
  </div>

  <div class="person">
    <p class="person__name">Your Long Name</p>
    <p class="person__title">Managing Director</p>
  </div>

  <div class="circuit-art" role="img" aria-label="Microchip with circuit traces spreading across the card"></div>

  <div class="contact-band">
    <p class="contact-band__row">
      <svg viewBox="0 0 12 12" fill="none" stroke="currentColor" stroke-width="1.3"><rect x="3" y="0.8" width="6" height="10.4" rx="1"/><line x1="5" y1="9.4" x2="7" y2="9.4"/></svg>
      00.00.00.0000
    </p>
    <p class="contact-band__row">
      <svg viewBox="0 0 12 12" fill="currentColor"><path d="M0.5 2.5h11v7h-11z"/><path d="M0.5 2.5 6 7l5.5-4.5" fill="none" stroke="#1d1d1d" stroke-width="1"/></svg>
      yourname@yourwebsite.com
      <span class="contact-band__phone2">
        <svg viewBox="0 0 12 12" fill="currentColor"><path d="M1 4.2C1 2.6 3 1.6 6 1.6s5 1 5 2.6v.8H8.4V4L3.6 4v1H1z"/><path d="M3.4 6h5.2l1.6 4.4H1.8z"/></svg>
        00.00.00.0000
      </span>
    </p>
    <p class="contact-band__row">
      <svg viewBox="0 0 12 12" fill="none" stroke="currentColor" stroke-width="1.1"><circle cx="6" cy="6" r="5"/><ellipse cx="6" cy="6" rx="2.2" ry="5"/><line x1="1" y1="6" x2="11" y2="6"/></svg>
      www.yourwebsite.com
    </p>
  </div>

  <div class="motto-block">"Value First"</div>
</section>

<section class="card card--back" aria-label="Card back">
  <div class="quote-band"></div>
  <p class="quote">"Here is your Long Quote with Name"</p>
  <p class="quote__by">by ABCD name</p>
</section>

</body>
</html>
```